Pixel Loft Gigs website

Our business is a freelance marketplace for IT and Digital contractors. It will provide a way for companies to take advantage of specialist talent for small periods of time and engage with them on a flexible basis. Logo should be something that shows Knowledge, Agility, Unlocking. Modern, simple, genius.We are looking for a site that conveys three things:- To have great technology you need great software, great hardware and great people. No one argues with that. To spend your dollars wisely and to focus on your core business, you have Cloud software and Cloud Hardware. Are any of your people in the cloud?- 5 specialists for the cost of one generalist- Cloud, agile and communication are converging to make the business case for remote specialists irresistible, we can get you the people you need to get your projects done, today.

Target Market(s)

Businesses, Tech professionals, Sales People, Recruiters

Industry/Entity Type

Information Technology

Logo Text

PixelLoftGigs or PLG

Coding

Coded - Design and coding required

Number of Pages Required

5+ page

Font styles to use
Sans Serif

Colors

Designer to choose colors to be used in the design.

Requirements
Must have
• A beautiful landing page with a technical feel to it
• a nice slick graphic for the How it works...
• A look and feel that is consistent throughout
• Some moving text
Should not have
• ugly anything

```html
<!DOCTYPE html>
<html lang="en">
<head>
<meta charset="utf-8">
<title>Pixel Loft Gigs</title>
<link rel="stylesheet" href="https://fonts.googleapis.com/css2?family=Fira+Sans:wght@400;500;600;700;800&family=Lato:wght@700;900&display=swap">
<style>
:root{
  --blue:#0a29c4;
  --navy:#1f2340;
  --ink:#2b2b2b;
  --muted:#444;
  --hero-a:#f8f8f8;
  --hero-b:#e4e4e6;
  --band:#f1f1f3;
  --white:#fff;
  --social:#77777a;
}
*{box-sizing:border-box;margin:0;padding:0}
html,body{width:1200px;height:2807px;overflow:hidden}
body{position:relative;background:var(--white);font-family:"Fira Sans",sans-serif;color:var(--ink)}
.abs{position:absolute}

.site-header{position:absolute;left:0;top:0;width:1200px;height:105px;background:var(--white)}
.menu-toggle{left:84px;top:38px;width:26px}
.menu-toggle span{display:block;height:3px;background:var(--blue);margin-bottom:6px;border-radius:2px}
.menu-toggle span:nth-child(2){width:20px;margin-left:6px}
.brand{left:124px;top:25px;display:flex;align-items:center;gap:12px}
.brand-dot{width:40px;height:40px;border-radius:50%;background:var(--blue)}
.brand-name{font-family:"Lato",sans-serif;font-weight:900;font-size:22px;line-height:26px;color:var(--blue)}
.main-nav{left:383px;top:42px;display:flex;gap:36px}
.nav-link{font-family:"Lato",sans-serif;font-weight:700;font-size:15px;color:#333;letter-spacing:.3px;text-decoration:none}
.cta{left:960px;top:33px;width:159px;height:37px;border-radius:19px;background:var(--blue);color:var(--white);
  font-weight:600;font-size:16px;display:flex;align-items:center;justify-content:center}

.hero{position:absolute;left:0;top:105px;width:1200px;height:748px;
  background:radial-gradient(circle at 50% 45%,var(--hero-a) 0,#f0f0f1 45%,var(--hero-b) 100%)}
.hero-mark{left:553px;top:240px;width:96px;height:96px;border-radius:50%;background:var(--blue)}
.hero-title{left:0;top:338px;width:1200px;text-align:center;font-weight:800;font-size:58px;line-height:68px;color:var(--blue);letter-spacing:1px}
.hero-sub{left:0;top:485px;width:1200px;text-align:center;font-size:28px;color:#333;letter-spacing:.5px}
.hero-figure{left:560px;top:548px;width:80px;height:210px;border-radius:40px;
  background:linear-gradient(#e9c9a9,#a9adb8 40%,rgba(200,200,205,0))}

.role-card{width:217px;height:214px;border-radius:32px;display:flex;flex-direction:column;align-items:center;
  color:var(--white);box-shadow:0 14px 30px rgba(10,41,196,.18)}
.role-card svg{margin-top:26px}
.role-card .label{margin-top:18px;font-size:29px;font-weight:500;letter-spacing:.5px}
.card-blue{background:var(--blue)}
.card-navy{background:var(--navy)}

.section-title{left:0;width:1200px;text-align:center;font-weight:800;font-size:38px;color:var(--blue)}
.title-rule{left:566px;width:68px;height:4px;background:var(--blue)}

.diagram-art{left:325px;top:1170px;width:550px;height:550px;border-radius:50%;
  background:radial-gradient(circle,#fff 0,#f4f4f6 55%,#e6e6ea 100%);border:2px dotted #c4c4c8}
.hub{left:0;top:1382px;width:1200px;text-align:center;font-weight:800;font-size:112px;color:var(--blue);letter-spacing:2px}
.node{width:115px;height:115px;border-radius:50%;background:var(--blue);display:flex;align-items:center;justify-content:center;
  box-shadow:0 10px 26px rgba(10,41,196,.3)}
.node-title{font-size:22px;color:var(--blue);font-weight:400}
.node-text{font-size:15px;line-height:22px;color:var(--muted);width:210px}

.stats-band{position:absolute;left:0;top:2045px;width:1200px;height:520px;background:var(--band)}
.stat-card{width:217px;height:214px;border-radius:32px;display:flex;flex-direction:column;align-items:center;justify-content:center;color:var(--white)}
.stat-num{font-weight:800;font-size:54px;line-height:54px;letter-spacing:1px}
.stat-cap{font-weight:700;font-size:17px;line-height:22px;text-align:center}

.footer-badge{left:570px;top:2540px;width:60px;height:60px;border-radius:50%;background:var(--white);
  display:flex;align-items:center;justify-content:center;font-weight:800;font-size:16px;color:var(--blue)}
.footer-nav{left:383px;top:2624px}
.social{top:2690px;width:32px;height:32px;border-radius:50%;background:var(--social)}
.legal{left:0;top:2755px;width:1200px;height:52px;background:var(--navy);color:var(--white);
  font-size:11px;display:flex;align-items:center;justify-content:center}
</style>
</head>
<body>

<header class="site-header">
  <div class="abs menu-toggle"><span></span><span></span><span></span></div>
  <div class="abs brand"><div class="brand-dot"></div><div class="brand-name">PIXEL LOFT<br>GIGS</div></div>
  <nav class="abs main-nav">
    <a class="nav-link">HOW IT WORKS</a><a class="nav-link">LOGIN</a><a class="nav-link">SIGN UP</a><a class="nav-link">COMPANY</a>
  </nav>
  <div class="abs cta">Start Side Job</div>
</header>

<section class="hero" role="img" aria-label="Light grey backdrop with a network of connected polygon lines and a glowing human figure"></section>
<div class="abs hero-mark"></div>
<h1 class="abs hero-title">PIXEL LOFT<br>GIGS</h1>
<p class="abs hero-sub">Do You Want to be a....</p>
<div class="abs hero-figure" role="img" aria-label="Glowing wireframe figure walking forward"></div>

<div class="abs role-card card-blue" style="left:222px;top:767px">
  <svg width="86" height="86" viewBox="0 0 86 86" fill="none" stroke="#fff" stroke-width="3"><rect x="4" y="12" width="78" height="56" rx="4"/><rect x="12" y="20" width="62" height="40"/><path d="M33 68v10h20V68M16 6v6M30 6v6M44 6v6M58 6v6M70 6v6"/></svg>
  <div class="label">Gigger</div>
</div>
<div class="abs role-card card-navy" style="left:492px;top:767px">
  <svg width="86" height="86" viewBox="0 0 86 86" fill="none" stroke="#fff" stroke-width="3"><rect x="4" y="44" width="40" height="30" rx="3"/><circle cx="24" cy="18" r="14"/><circle cx="58" cy="34" r="12"/><path d="M40 82V66q18-14 36 0v16"/></svg>
  <div class="label">Customer</div>
</div>
<div class="abs role-card card-blue" style="left:762px;top:767px">
  <svg width="86" height="86" viewBox="0 0 86 86" fill="none" stroke="#fff" stroke-width="3"><circle cx="43" cy="43" r="22"/><path d="M43 4v12M43 70v12M4 43h12M70 43h12M14 14l9 9M72 14l-9 9M14 72l9-9M72 72l-9-9"/></svg>
  <div class="label">Affiliate</div>
</div>

<h2 class="abs section-title" style="top:1055px">How it works</h2>
<div class="abs title-rule" style="top:1112px"></div>

<div class="abs diagram-art" role="img" aria-label="Ring of thin grey line icons for devices, cloud, data and analytics"></div>
<svg class="abs" style="left:0;top:0" width="1200" height="2000" fill="none" stroke="#0a29c4" stroke-width="1.2">
  <line x1="296" y1="1308" x2="480" y2="1445"/>
  <line x1="906" y1="1310" x2="720" y2="1447"/>
  <line x1="600" y1="1502" x2="600" y2="1748"/>
  <g fill="#0a29c4" stroke="none"><circle cx="480" cy="1445" r="6"/><circle cx="720" cy="1447" r="6"/><circle cx="600" cy="1502" r="7"/></g>
</svg>
<div class="abs hub">PLG</div>

<div class="abs node" style="left:187px;top:1217px">
  <svg width="60" height="60" viewBox="0 0 60 60" fill="none" stroke="#fff" stroke-width="3"><path d="M4 18h12l14 6 14-6h12v22H44L30 52 16 40H4z"/></svg>
</div>
<div class="abs node-title" style="left:194px;top:1350px">BUSINESS</div>
<p class="abs node-text" style="left:86px;top:1387px;text-align:right">Lorem ipsum dolor sit amet, consectetur adipiscing elit, sed do eiusmod tempor incididunt ut labore et dolore magna aliqua. Ut enim ad minim veniam, quis nostrud</p>

<div class="abs node" style="left:895px;top:1217px">
  <svg width="60" height="60" viewBox="0 0 60 60" fill="none" stroke="#fff" stroke-width="3"><circle cx="30" cy="12" r="8"/><circle cx="10" cy="26" r="8"/><circle cx="50" cy="26" r="8"/><path d="M30 24v30"/></svg>
</div>
<div class="abs node-title" style="left:900px;top:1350px">AFFILIATE</div>
<p class="abs node-text" style="left:900px;top:1389px">Lorem ipsum dolor sit amet, consectetur adipiscing elit, sed do eiusmod tempor incididunt ut labore et dolore magna aliqua. Ut enim ad minim veniam, quis nostrud</p>

<div class="abs node" style="left:543px;top:1748px">
  <svg width="60" height="60" viewBox="0 0 60 60" fill="none" stroke="#fff" stroke-width="3"><circle cx="30" cy="20" r="13"/><path d="M8 56q22-26 44 0z"/></svg>
</div>
<div class="abs node-title" style="left:676px;top:1781px">SPECIALISTS</div>
<p class="abs node-text" style="left:676px;top:1820px">Lorem ipsum dolor sit amet, consectetur adipiscing elit, sed do eiusmod tempor incididunt ut labore et dolore magna aliqua. Ut enim ad minim veniam, quis nostrud</p>

<section class="stats-band"></section>
<h2 class="abs section-title" style="top:2112px">Stats</h2>
<div class="abs title-rule" style="top:2169px"></div>

<div class="abs stat-card card-blue" style="left:222px;top:2248px"><div class="stat-num">100%</div><div class="stat-cap">Of stats<br>on services</div></div>
<div class="abs stat-card card-navy" style="left:492px;top:2248px"><div class="stat-num">70%</div><div class="stat-cap">Of stats<br>on services</div></div>
<div class="abs stat-card card-blue" style="left:762px;top:2248px"><div class="stat-num">90%</div><div class="stat-cap">Of stats<br>on services</div></div>

<div class="abs footer-badge">PLG</div>
<nav class="abs main-nav footer-nav">
  <a class="nav-link">HOW IT WORKS</a><a class="nav-link">LOGIN</a><a class="nav-link">SIGN UP</a><a class="nav-link">COMPANY</a>
</nav>
<div class="abs social" style="left:518px"></div>
<div class="abs social" style="left:562px"></div>
<div class="abs social" style="left:606px"></div>
<div class="abs social" style="left:649px"></div>

<footer class="abs legal">© 2019 | www.pixelloftgigs.example</footer>

</body>
</html>
```